IT company website design

Require a home page and an inner page designed for a company located in Ohio. The company deals with a wide range of IT services like Software development, IT based education services such as digital textbooks and BPO

Would like to get a Home page for the website and an inner page to be designed.

Design must be modern, clean and very professional. The home page should have a carousel of our services for which content will be provided.

It should give a feel that we are a large company to our prospective customers.
Updates

Hi,
In the few designs I have got for the home page, there are mockups with unwanted content/blocks like ex. latest blog posts or similar blocks. Kindly note that, we don't want this. Please follow the information about content on the home page as mentioned in the project brief. Designers, who have already submitted designs, if you can remove the unwanted blocks, it will be really appreciated.

Thanks.

I have received over 9 designs for this project, but none of them seem to be custom designed for my needs. They are just re-use of previous designs and look very out dated. Looking for fresh, clean designs following latest design trends like the ones you see in pixelbazaar etc.

If you can provide me a design that meets my expectations, I can definitely UP my budget for you .

Industry/Entity Type

Education

Requirements
Must have
• > > Home page > >
Home page will have

* Top Menu: Home, About Us, Solutions, Services, Contact us (should have space to accommodate for more)

* Should have a flash carousel/slide show. Each slide should be about a service we provide. Ex. a slide for bpo will have the content "Bridging the quality and cost divide in outsourcing" It should be depicted by an illustration or photograph. If you are going to use photograph, please use ones for framelode.com

* Textual content of about 200 words which we will provide

* Links in the footer along with a copyright, legal notice etc.

* Importantly, the home page should have 2 fancy buttons for "Member Login" and "Online Tutoring"

> > Inner pages > >
Will be mainly textual content explaining each of the service so, should have space for lots of textual content, with a fancy, page title (usually the service name). All inner pages should also have a side menu or something like that from where users can have a one click access to all our services.

Our logo is blue in color. with color code "0080FB". It just a stylized D with rest of the text i.e Quorvane Tech Inc. our logo is of the proportion. 1:5 i.e 60px height, 300px wide. We can proportionately increase or decrease the dimensions as necessary. Color combination of the sight should be something that will go with this.

```html
<!DOCTYPE html>
<html lang="en">
<head>
<meta charset="utf-8">
<title>Quorvane Tech Inc. — Home</title>
<link href="https://fonts.googleapis.com/css2?family=Ubuntu:wght@300;400;500;700&display=swap" rel="stylesheet">
<style>
  :root {
    --navy: #16213f;
    --navy-deep: #0d1530;
    --brand: #0080fb;
    --nav-text: #c9d6ee;
    --panel: #ececec;
    --card: #f7f7f7;
    --heading: #555b63;
    --body: #8a8f96;
    --link: #1f5fb5;
    --row-active: #d3dcf2;
    --green: #9bc52a;
    --green-dark: #4f6a0f;
    --blue-btn: #1f8fe6;
    --foot-text: #b9c4dc;
    --foot-small: #7f8aa6;
  }
  * { box-sizing: border-box; margin: 0; padding: 0; }
  html, body { width: 1200px; height: 1174px; overflow: hidden; background: #fff; }
  body { font-family: "Ubuntu", sans-serif; }
  .page { position: relative; width: 1200px; height: 1174px; overflow: hidden; background: #fff; }
  .abs { position: absolute; }

  /* header */
  .site-header { left: 0; top: 0; width: 1200px; height: 74px; background: linear-gradient(#1b2747, var(--navy)); border-bottom: 1px solid #3a4766; }
  .brand { left: 172px; top: 23px; display: flex; align-items: center; gap: 8px; font-size: 24px; line-height: 28px; font-weight: 500; color: var(--brand); letter-spacing: -0.4px; white-space: nowrap; }
  .brand-mark { width: 16px; height: 16px; border-radius: 50%; background: var(--brand); }
  .main-nav { left: 0; top: 33px; width: 1200px; height: 24px; font-size: 12.5px; color: var(--nav-text); }
  .main-nav a { position: absolute; top: 0; color: inherit; text-decoration: none; white-space: nowrap; padding-bottom: 6px; }
  .main-nav a.current { border-bottom: 1px dotted #5b8fd8; padding-left: 8px; padding-right: 8px; }
  .search { left: 891px; top: 26px; width: 124px; height: 24px; border-radius: 12px; background: #f1f2f4; border: 1px solid #c9ccd2; font-size: 11px; color: #9a9ea6; padding: 4px 10px; }
  .search svg { position: absolute; right: 8px; top: 3px; }
  .search .sep { position: absolute; right: 32px; top: 4px; width: 1px; height: 14px; background: #b0b4bb; }

  /* hero */
  .hero { left: 0; top: 75px; width: 1200px; height: 325px;
    background: radial-gradient(ellipse 480px 240px at 560px 160px, #1769b8 0%, #0f3a8c 45%, #142067 75%, #170f3a 100%); }
  .hero-title { left: 190px; top: 158px; color: #eef3fb; font-size: 40px; line-height: 40px; font-weight: 300; letter-spacing: -0.6px; text-shadow: 0 2px 3px rgba(0,0,0,.4); white-space: nowrap; }
  .hero-title span { display: block; padding-left: 4px; font-size: 35px; }
  .cta { display: flex; align-items: center; justify-content: space-between; border-radius: 26px; padding: 0 10px 0 28px; font-weight: 700; line-height: 17px; box-shadow: 0 6px 8px rgba(0,0,0,.35); }
  .cta-label { font-size: 19px; letter-spacing: -0.5px; }
  .cta-member { left: 176px; top: 294px; width: 155px; height: 53px; background: linear-gradient(#c2e347, var(--green) 50%, #7aa315); color: var(--green-dark); }
  .cta-tutor { left: 386px; top: 296px; width: 158px; height: 54px; background: linear-gradient(#63bdf8, var(--blue-btn) 50%, #1266c9); color: #0c3f86; }
  .cta-arrow { width: 28px; height: 28px; border-radius: 50%; display: flex; align-items: center; justify-content: center; }
  .cta-member .cta-arrow { background: #5e7f12; }
  .cta-tutor .cta-arrow { background: #1a63bf; }

  /* content */
  .content-panel { left: 172px; top: 400px; width: 843px; height: 606px; background: var(--panel); }
  .intro-card { left: 172px; top: 400px; width: 513px; height: 300px; background: linear-gradient(#fafafa, var(--panel)); }
  .section-title { color: var(--heading); font-size: 23px; font-weight: 400; letter-spacing: -0.3px; white-space: nowrap; }
  .copy { color: var(--body); font-size: 12.5px; line-height: 19.4px; }
  .intro-title { left: 241px; top: 455px; }
  .intro-copy { left: 242px; top: 499px; width: 395px; }

  .service-list { left: 685px; top: 415px; width: 330px; height: 284px; background: var(--card); border: 1px solid #dcdcdc; }
  .service { position: absolute; left: 0; width: 330px; height: 90px; }
  .service.active { background: var(--row-active); }
  .service-icon { position: absolute; left: 16px; top: 12px; width: 68px; height: 66px; border-radius: 4px; background: linear-gradient(#8ab0f1, #4c76d3); box-shadow: 0 4px 6px rgba(40,60,120,.35); display: flex; align-items: center; justify-content: center; }
  .service-name { position: absolute; left: 102px; top: 24px; font-size: 13.5px; font-weight: 500; color: var(--link); white-space: nowrap; }
  .service-text { position: absolute; left: 102px; top: 44px; font-size: 9.8px; line-height: 13px; color: #5d6269; letter-spacing: .2px; white-space: nowrap; }
  .service-go { position: absolute; right: 17px; top: 28px; width: 33px; height: 33px; border-radius: 50%; background: #c9cacd; display: flex; align-items: center; justify-content: center; }
  .service.active .service-go { background: #a7b8e6; }

  .product-card { left: 205px; top: 743px; width: 810px; height: 236px; background: linear-gradient(#f4f4f4, #fbfbfb); border: 1px solid #e2e2e2; border-radius: 8px 0 0 8px; }
  .product-title { left: 243px; top: 780px; font-size: 24px; }
  .product-copy { left: 243px; top: 820px; width: 395px; }
  .product-badge { left: 645px; top: 821px; width: 79px; height: 79px; border-radius: 7px; background: linear-gradient(#3d86ea, #1d57c5); box-shadow: 0 4px 6px rgba(0,0,0,.25); }
  .divider { left: 755px; top: 785px; width: 1px; height: 150px; background: #d8d8d8; }
  .aside-copy { left: 785px; top: 820px; width: 222px; font-size: 11.4px; }
  .aside-copy a { color: var(--brand); text-decoration: none; white-space: nowrap; }

  /* footer */
  .site-footer { left: 0; top: 1006px; width: 1200px; height: 168px; background: linear-gradient(#1c2850, var(--navy-deep)); }
  .foot-nav { left: 171px; top: 1080px; display: flex; gap: 23px; font-size: 12.5px; color: var(--foot-text); }
  .foot-tag { left: 776px; top: 1030px; font-size: 10.5px; font-weight: 500; color: #aab4c8; letter-spacing: .2px; white-space: nowrap; }
  .social { left: 778px; top: 1056px; display: flex; gap: 10px; }
  .social span { width: 39px; height: 39px; border-radius: 50%; background: #323f5f; border: 2px solid #3e4c6e; }
  .foot-rule { left: 171px; top: 1113px; width: 820px; height: 1px; background: #2e3a5a; }
  .legal { left: 170px; top: 1131px; font-size: 8.4px; line-height: 11px; color: var(--foot-small); white-space: nowrap; }
</style>
</head>
<body>
<div class="page">

  <header class="site-header abs"></header>
  <div class="brand abs"><span class="brand-mark"></span>Quorvane Tech Inc.</div>
  <nav class="main-nav abs">
    <a class="current" href="#" style="left:473px">Home</a>
    <a href="#" style="left:540px">About us</a>
    <a href="#" style="left:617px">Solutions</a>
    <a href="#" style="left:695px">Services</a>
    <a href="#" style="left:766px">Contact us</a>
  </nav>
  <div class="search abs">Search<span class="sep"></span>
    <svg width="18" height="18" viewBox="0 0 18 18"><circle cx="7" cy="7" r="5" fill="none" stroke="#8d9199" stroke-width="1.6"/><path d="M11 11l5 5" stroke="#8d9199" stroke-width="2"/></svg>
  </div>

  <section class="hero abs" role="img" aria-label="Glowing blue technology backdrop with a soft dotted pattern"></section>
  <h1 class="hero-title abs">Bridging the quality and cost<span>divide in outsourcing</span></h1>
  <a class="cta cta-member abs"><span class="cta-label">MEMBER<br>Login</span><span class="cta-arrow"><svg width="12" height="12" viewBox="0 0 12 12"><path d="M4 2l4 4-4 4" fill="none" stroke="#e4f39b" stroke-width="2.4"/></svg></span></a>
  <a class="cta cta-tutor abs"><span class="cta-label">ONLINE<br>Tutoring</span><span class="cta-arrow"><svg width="12" height="12" viewBox="0 0 12 12"><path d="M4 2l4 4-4 4" fill="none" stroke="#bfe2ff" stroke-width="2.4"/></svg></span></a>

  <main>
    <div class="content-panel abs"></div>
    <div class="intro-card abs"></div>
    <h2 class="section-title intro-title abs">Looking for Dedicated Developer?</h2>
    <p class="copy intro-copy abs">Lorem ipsum dolor sit amet, consectetuer adipiscing elit. Aenean commodo ligula eget dolor. Aenean massa. Cum sociis natoque penatibus et magnis dis parturient montes, nascetur ridiculus mus. Donec quam felis, ultricies nec, pellentesque eu, pretium quis, sem. Nulla consequat massa quis enim. Donec pede justo, fringilla vel, aliquet nec, vulputate eget, arcu. In enim justo, rhoncus ut, imperdiet a, venenatis vitae, justo.</p>

    <div class="service-list abs">
      <div class="service" style="top:0">
        <div class="service-icon"><svg width="40" height="34" viewBox="0 0 40 34"><rect x="3" y="3" width="34" height="23" rx="2" fill="#2f4f9e" stroke="#dbe6ff" stroke-width="2"/><path d="M14 8l0 10 3-3 3 5 2-1-3-5 4 0z" fill="#dbe6ff"/><rect x="15" y="27" width="10" height="4" fill="#dbe6ff"/></svg></div>
        <div class="service-name">Web Development</div>
        <div class="service-text">Lorem ipsum dolor sit amet, con<br>sectetuer adipiscing elit, sed</div>
        <div class="service-go"><svg width="12" height="12" viewBox="0 0 12 12"><path d="M4 2l4 4-4 4" fill="none" stroke="#fff" stroke-width="2.4"/></svg></div>
      </div>
      <div class="service active" style="top:91px">
        <div class="service-icon"><svg width="40" height="40" viewBox="0 0 40 40"><path d="M8 32L24 16M30 6a6 6 0 0 0-7 8l3 3a6 6 0 0 0 8-7l-4 3-3-3z" fill="none" stroke="#1d2f66" stroke-width="4" stroke-linecap="round"/><path d="M8 8l24 24" stroke="#1d2f66" stroke-width="4" stroke-linecap="round"/></svg></div>
        <div class="service-name" style="left:97px">Custom Software</div>
        <div class="service-text" style="left:97px">Lorem ipsum dolor sit amet, con<br>sectetuer adipiscing elit, sed</div>
        <div class="service-go"><svg width="12" height="12" viewBox="0 0 12 12"><path d="M4 2l4 4-4 4" fill="none" stroke="#fff" stroke-width="2.4"/></svg></div>
      </div>
      <div class="service" style="top:182px">
        <div class="service-icon" style="left:20px"><svg width="42" height="42" viewBox="0 0 42 42"><circle cx="21" cy="21" r="12" fill="none" stroke="#1d2f66" stroke-width="7" stroke-dasharray="6 3.4"/><circle cx="21" cy="21" r="10" fill="none" stroke="#1d2f66" stroke-width="4"/><circle cx="21" cy="21" r="5" fill="#8ab0f1"/></svg></div>
        <div class="service-name" style="left:99px">Business Applications</div>
        <div class="service-text" style="left:97px">Lorem ipsum dolor sit amet, con<br>sectetuer adipiscing elit, sed</div>
        <div class="service-go"><svg width="12" height="12" viewBox="0 0 12 12"><path d="M4 2l4 4-4 4" fill="none" stroke="#fff" stroke-width="2.4"/></svg></div>
      </div>
    </div>

    <div class="product-card abs"></div>
    <h2 class="section-title product-title abs">The easiest all-in-one web software</h2>
    <p class="copy product-copy abs">Lorem ipsum dolor sit amet, consectetuer adipiscing elit. Aenean commodo ligula eget dolor. Aenean massa. Cum sociis natoque penatibus et magnis dis parturient montes, nascetur ridiculus mus. Donec quam felis, ultricies nec, pellentesque eu, pretium quis, sem. Nullam dictum felis eu pede mollis pretium.</p>
    <div class="product-badge abs" role="img" aria-label="Product box icon for the pro version of the web software"></div>
    <div class="divider abs"></div>
    <p class="copy aside-copy abs">Lorem ipsum dolor sit amet, consectetuer adipiscing elit. Aenean commodo ligula eget dolor. Aenean massa. Cum sociis natoque penatibus et magnis dis mus parturient montes. <a href="#">Learn more ▸</a></p>
  </main>

  <footer class="site-footer abs"></footer>
  <nav class="foot-nav abs"><span>Home</span><span>About us</span><span>Solutions</span><span>Services</span><span>Contact us</span></nav>
  <div class="foot-tag abs">GET TO KNOW US...&nbsp;&nbsp;WHEREVER YOU ARE</div>
  <div class="social abs"><span></span><span></span><span></span><span></span></div>
  <div class="foot-rule abs"></div>
  <p class="legal abs">Privacy Policy | Refund &amp; Cancellation Policy | Sitemap<br>copyright © 2011 - Quorvane Tech Inc., All Rights Reserved. Software and Web Development Company. All rights reserved</p>

</div>
</body>
</html>
```